Halvo KT Biz Card Design

Residential / Commercial/ Emergency

Industry/Entity Type

Residential

Contact Information for Business Card

Tomas Welker
President
PO Box 4827
East Quogue, NY 11942
tomas@halvo-kt.com
631.555.0172
855.HALVO.KT
www.halvo-kt.com
FB: Halvo KT
Twitter: HALVO KT

```html
<!DOCTYPE html>
<html lang="en">
<head>
<meta charset="utf-8">
<title>Halvo KT – Services</title>
<link href="https://fonts.googleapis.com/css2?family=Lato:wght@400&display=swap" rel="stylesheet">
<style>
  :root {
    --bg: #23272b;
    --panel: #ec8922;
    --ink: #ffffff;
    --social-1: #8fb6e2;
    --social-2: #8ad6f2;
    --social-3: #e8676f;
  }
  html, body {
    margin: 0;
    padding: 0;
    overflow: hidden;
    background: var(--bg);
  }
  .canvas {
    position: relative;
    width: 1200px;
    height: 720px;
    background: var(--bg);
    overflow: hidden;
    font-family: "Lato", Arial, sans-serif;
  }
  .service-panel {
    position: absolute;
    left: 0;
    top: 0;
  }
  .service-panel path {
    fill: var(--panel);
  }
  .service-list {
    position: absolute;
    left: 322px;
    top: 182px;
    width: 600px;
    margin: 0;
    padding: 0;
    list-style: none;
    text-align: center;
    color: var(--ink);
    font-size: 31px;
    line-height: 37.4px;
    letter-spacing: 0.2px;
  }
  .social-links {
    position: absolute;
    left: 949px;
    top: 120px;
    display: flex;
    gap: 6px;
  }
  .social-links span {
    display: block;
    width: 42px;
    height: 42px;
    border-radius: 11px;
  }
  .social-links .social-a { background: var(--social-1); }
  .social-links .social-b { background: var(--social-2); }
  .social-links .social-c { background: var(--social-3); }
</style>
</head>
<body>
<main class="canvas">
  <div class="social-links" aria-label="Social profiles">
    <span class="social-a"></span>
    <span class="social-b"></span>
    <span class="social-c"></span>
  </div>

  <svg class="service-panel" width="1200" height="720" viewBox="0 0 1200 720" aria-hidden="true">
    <path d="M 268 172 L 1090 172 Q 1110 172 1102 194 L 985 532 Q 970 565 940 565 L 120 565 Q 102 565 109 546 L 228 204 Q 240 172 268 172 Z"/>
  </svg>

  <ul class="service-list">
    <li>AERO FARMING</li>
    <li>CELLULAR TOWERS</li>
    <li>COMM/IND SECURITY</li>
    <li>CONSTRUCTION</li>
    <li>INSPECTIONS</li>
    <li>LUXURY YACHTS</li>
    <li>POST DISASTER VIEWS</li>
    <li>PUBLIC SAFETY</li>
    <li>SEARCH &amp; RESCUE</li>
    <li>SURVEYS</li>
  </ul>
</main>
</body>
</html>
```